Law Firm Logo and Business Card Design

I need a logo and business card design for a law firm I just started. The law firm is named Law Office of Doreen K. Ashworth, LLC. The type of law I practice is Family Law, which includes divorce, custody, child support, alimony, property division, and the like. I would like to see designs that are unique and modern, yet sophisticated. I would also like to use the logo/design for my letterhead. I am not opposed to using some form of the scales of justice although I'd like something other than the typical, old fashioned scales of justice. I had considered a house made out of puzzle pieces with one puzzle piece pulled away from the others, with the logo text reading "Guiding your family forward, one step at a time." However, I don't want that particular design to look juvenile. I also would not be opposed to some form of my initials on the logo -- my initials are DKA. I am open to any other ideas you may have. I would like to see raised designs/lettering, and/or metallic finish. I like the colors black, white, gold, silver, and/or teal.

Industry/Entity Type

Law Firm

```html
<!DOCTYPE html>
<html lang="en">
<head>
<meta charset="utf-8">
<title>Law Office of Doreen K. Ashworth, LLC — Business Card</title>
<link rel="stylesheet" href="https://fonts.googleapis.com/css2?family=Archivo+Narrow:wght@700&family=Archivo:ital,wght@1,700&family=Questrial&display=swap">
<style>
  :root {
    --page: #f4f4f4;
    --card-white: #ffffff;
    --card-black: #141414;
    --card-black-deep: #0a0a0a;
    --gold: #b9833f;
    --gold-light: #d4a05c;
    --ink: #111111;
    --grey-text: #c9c9c9;
    --tagline-light: #e6e6e6;
  }
  * { box-sizing: border-box; margin: 0; padding: 0; }
  html, body { width: 1200px; height: 900px; overflow: hidden; }
  body {
    background: var(--page);
    display: flex;
    align-items: center;
    justify-content: center;
    gap: 44px;
  }
  .card {
    width: 540px;
    height: 310px;
    border-radius: 22px;
    overflow: hidden;
    position: relative;
    box-shadow: 0 10px 28px rgba(0,0,0,0.18);
  }

  /* Front */
  .card-front { background: var(--card-white); display: flex; flex-direction: column; }
  .front-header {
    height: 142px;
    display: flex;
    align-items: center;
    padding: 0 22px;
    gap: 18px;
  }
  .brand-square {
    width: 86px; height: 86px;
    border-radius: 10px;
    background: var(--gold);
    flex: none;
  }
  .firm-name {
    font-family: "Archivo Narrow", sans-serif;
    font-weight: 700;
    font-size: 24px;
    color: var(--ink);
    letter-spacing: 0.2px;
    white-space: nowrap;
  }
  .tagline-band {
    height: 20px;
    background: var(--gold);
    display: flex;
    align-items: center;
    padding-left: 20px;
    font-family: "Archivo", sans-serif;
    font-style: italic;
    font-weight: 700;
    font-size: 11px;
    letter-spacing: 3.2px;
    color: #fff;
    text-transform: uppercase;
    white-space: nowrap;
  }
  .front-contact {
    flex: 1;
    background: radial-gradient(ellipse at 30% 20%, #222 0%, var(--card-black) 55%, var(--card-black-deep) 100%);
    padding: 14px 22px;
    list-style: none;
    font-family: "Questrial", sans-serif;
    font-size: 16px;
    color: var(--grey-text);
  }
  .contact-line { display: flex; align-items: center; gap: 8px; height: 24px; }
  .contact-line svg { width: 15px; height: 15px; flex: none; fill: var(--gold); stroke: var(--gold); }

  /* Back */
  .card-back {
    background: radial-gradient(ellipse at 50% 35%, #262626 0%, var(--card-black) 55%, var(--card-black-deep) 100%);
    display: flex;
    flex-direction: column;
    align-items: center;
    justify-content: center;
  }
  .back-brand {
    display: flex;
    flex-direction: column;
    align-items: center;
    gap: 20px;
    margin-top: -28px;
  }
  .back-square {
    width: 64px; height: 64px;
    border-radius: 8px;
    background: var(--gold);
  }
  .back-name {
    font-family: "Archivo Narrow", sans-serif;
    font-weight: 700;
    font-size: 26px;
    color: var(--gold-light);
    text-align: center;
    white-space: nowrap;
  }
  .back-tagline {
    position: absolute;
    bottom: 30px;
    left: 0; right: 0;
    text-align: center;
    font-family: "Archivo Narrow", sans-serif;
    font-weight: 700;
    font-size: 12px;
    letter-spacing: 3.6px;
    color: var(--tagline-light);
    text-transform: uppercase;
    white-space: nowrap;
  }
</style>
</head>
<body>

<section class="card card-front" aria-label="Business card front">
  <header class="front-header">
    <div class="brand-square"></div>
    <h1 class="firm-name">Law Office of Doreen K. Ashworth, LLC</h1>
  </header>
  <div class="tagline-band">Guiding your family forward, one step at a time</div>
  <ul class="front-contact">
    <li class="contact-line">
      <svg viewBox="0 0 16 16"><path stroke="none" d="M3 1l3 3-1.6 2c.8 1.9 2.4 3.5 4.6 4.6L11 9l3 3-2 3C6 14 2 10 1 3z"/></svg>
      555-014-2290
    </li>
    <li class="contact-line">
      <svg viewBox="0 0 16 16"><rect stroke="none" x="2" y="6" width="12" height="8" rx="1"/><rect stroke="none" x="4" y="1" width="8" height="4"/></svg>
      555-018-6624
    </li>
    <li class="contact-line">
      <svg viewBox="0 0 16 16" fill="none"><circle cx="8" cy="8" r="6.5" fill="none" stroke-width="1.4"/><ellipse cx="8" cy="8" rx="2.8" ry="6.5" fill="none" stroke-width="1.2"/><path d="M1.5 8h13" stroke-width="1.2"/></svg>
      www.ashworthfamilylaw.com
    </li>
    <li class="contact-line">
      <svg viewBox="0 0 16 16"><rect stroke="none" x="1" y="3" width="14" height="10" rx="1"/><path d="M1.5 4L8 9l6.5-5" fill="none" stroke="#141414" stroke-width="1.3"/></svg>
      info@ashworthfamilylaw.com
    </li>
    <li class="contact-line">
      <svg viewBox="0 0 16 16"><path stroke="none" d="M8 1.5L1 8h2v6.5h4v-4h2v4h4V8h2z"/></svg>
      2087 Linden Grove Rd. Canada
    </li>
  </ul>
</section>

<section class="card card-back" aria-label="Business card back">
  <div class="back-brand">
    <div class="back-square"></div>
    <p class="back-name">Law Office of Doreen K. Ashworth, LLC</p>
  </div>
  <p class="back-tagline">Guiding your family forward, one step at a time</p>
</section>

</body>
</html>
```